Pelvo BUSINESS CARD

Design an attention-grabbing business cards. Draw inspiration from the provided logo file. Please use the same font style as in the logo.
the back side of the card is for accent/decoration.

Contact Information for Business Card

PLEASE USE PROVIDED BUSINESS CARD SAMPLE

Other font styles liked:
• MIRVALLE

Colors
EB3D1F
EC4F4E
F09395
F8D3D4
FCEDEE

Requirements
Must have
• RED, BLACK COLORS, SOLID BACK COLOR
Nice to have
• MAKE IT FANCY

```html
<!DOCTYPE html>
<html lang="en">
<head>
<meta charset="utf-8">
<title>Pelvo Business Card</title>
<link href="https://fonts.googleapis.com/css2?family=Orbitron:wght@500;700&family=Open+Sans:wght@400&display=swap" rel="stylesheet">
<style>
  :root {
    --stage: #2f2f31;
    --red: #e0393f;
    --red-soft: #e8585c;
    --ink: #2b2b2b;
    --paper: #ffffff;
    --grey: #6a6a6a;
  }
  * { box-sizing: border-box; margin: 0; padding: 0; }
  html, body { width: 1200px; height: 998px; overflow: hidden; }
  body { background: var(--stage); position: relative; font-family: "Orbitron", sans-serif; }

  .card { position: absolute; width: 620px; height: 354px; box-shadow: 0 12px 30px rgba(0,0,0,.5); }

  /* back side */
  .card-back { left: 60px; top: 100px; background: var(--red); }
  .card-back .pattern-area {
    position: absolute; inset: 0;
    background: linear-gradient(135deg, var(--red) 0%, var(--red-soft) 50%, var(--red) 100%);
  }
  .card-back .mark {
    position: absolute; left: 50%; top: 50%; transform: translate(-50%, -50%);
    display: flex; align-items: center; gap: 12px;
    color: var(--paper); font-weight: 700; font-size: 30px; letter-spacing: 3px;
  }
  .mark .dot { width: 22px; height: 22px; border-radius: 50%; background: var(--paper); }

  /* front side */
  .card-front { left: 530px; top: 560px; background: var(--paper); color: var(--ink); }
  .brand { position: absolute; right: 40px; top: 40px; display: flex; align-items: center; gap: 12px; }
  .brand .square { width: 46px; height: 46px; background: var(--ink); }
  .brand-name { font-weight: 700; font-size: 44px; letter-spacing: 3px; line-height: 1; color: var(--ink); }
  .brand-tagline { font-family: "Open Sans", sans-serif; font-size: 9px; letter-spacing: 1.5px; color: var(--grey); margin-top: 3px; }
  .rule-top { position: absolute; right: 30px; top: 112px; width: 330px; height: 1.5px; background: var(--ink); }

  .person { position: absolute; left: 36px; top: 150px; }
  .person-name { color: var(--red); font-weight: 700; font-size: 30px; letter-spacing: 2px; }
  .person-title { font-weight: 500; font-size: 14px; letter-spacing: 2px; margin-top: 6px; }
  .rule-mid { position: absolute; left: 36px; top: 222px; width: 250px; height: 1.5px; background: var(--ink); }

  .contacts { position: absolute; left: 36px; top: 236px; list-style: none; }
  .contacts li { display: flex; align-items: center; gap: 10px; font-weight: 500; font-size: 14px; letter-spacing: 1px; height: 24px; }
  .contacts svg { width: 16px; height: 16px; flex: none; }

  .address { position: absolute; right: 36px; top: 170px; text-align: right; font-weight: 500; font-size: 15px; letter-spacing: 1.5px; line-height: 1.5; }
</style>
</head>
<body>

<section class="card card-back">
  <div class="pattern-area" role="img" aria-label="Repeating pattern of faint brand emblems on red"></div>
  <div class="mark"><span class="dot"></span><span>PELVO</span></div>
</section>

<section class="card card-front">
  <div class="brand">
    <span class="square"></span>
    <div>
      <div class="brand-name">PELVO</div>
      <div class="brand-tagline">FREIGHT WITH SPIRIT</div>
    </div>
  </div>
  <div class="rule-top"></div>

  <div class="person">
    <div class="person-name">TOMAS REYNA</div>
    <div class="person-title">PRESIDENT</div>
  </div>
  <div class="rule-mid"></div>

  <ul class="contacts">
    <li>
      <svg viewBox="0 0 16 16"><circle cx="8" cy="8" r="8" fill="#e0393f"/><path d="M5 4.5h2l.6 2-1 .8a5 5 0 0 0 2.1 2.1l.8-1 2 .6v2a1 1 0 0 1-1 1A7 7 0 0 1 4 5.5a1 1 0 0 1 1-1z" fill="#fff"/></svg>
      555-204-3817
    </li>
    <li>
      <svg viewBox="0 0 16 16"><circle cx="8" cy="8" r="8" fill="#e0393f"/><rect x="5.5" y="3.5" width="5" height="9" rx="1" fill="#fff"/><circle cx="8" cy="11" r=".7" fill="#e0393f"/></svg>
      555 318-6042
    </li>
    <li>
      <svg viewBox="0 0 16 16"><circle cx="8" cy="8" r="8" fill="#e0393f"/><rect x="4" y="5" width="8" height="6" fill="#fff"/><path d="M4 5l4 3.2L12 5" stroke="#e0393f" fill="none" stroke-width="1"/></svg>
      TREYNA PELVO-LLC.COM
    </li>
    <li>
      <svg viewBox="0 0 16 16"><circle cx="8" cy="8" r="8" fill="#e0393f"/><circle cx="8" cy="8" r="4.2" fill="none" stroke="#fff" stroke-width="1.1"/><path d="M3.8 8h8.4M8 3.8c-2 2.5-2 5.9 0 8.4M8 3.8c2 2.5 2 5.9 0 8.4" stroke="#fff" fill="none" stroke-width="1"/></svg>
      WWW.PELVO-LLC.COM
    </li>
  </ul>

  <div class="address">1184 N. 250<br>EAST, HARLOW,<br>IN, 40218</div>
</section>

</body>
</html>
```